Brix2Key Header

I want a professional Letterhead for my law firm. I'm attaching the letterhead I currently use in Word and PDF form. I'm also attaching my logo, and an example header that I like.

```html
<!DOCTYPE html>
<html lang="en">
<head>
<meta charset="utf-8">
<title>Brix2Key Letterhead</title>
<link href="https://fonts.googleapis.com/css2?family=Arimo:wght@400;700&family=Tinos:ital,wght@0,400;0,700;1,400&display=swap" rel="stylesheet">
<style>
  :root {
    --ink: #1a1a1a;
    --panel: #313235;
    --blue: #0a68b8;
    --green: #5a8a55;
    --rule: #6a9a5a;
    --grey-text: #333;
    --backdrop: #e6e6e6;
    --paper: #ffffff;
  }
  * { margin: 0; padding: 0; box-sizing: border-box; }
  html, body { width: 1009px; height: 1200px; overflow: hidden; background: var(--backdrop); }
  .sheet {
    position: absolute; left: 80px; top: 0; width: 849px; height: 1200px;
    background: var(--paper); overflow: hidden;
    font-family: "Tinos", "Times New Roman", serif; color: var(--ink);
  }
  .masthead { position: absolute; left: 0; top: 0; width: 849px; height: 118px; }
  .masthead-shape { position: absolute; left: 0; top: 0; }
  .brand { position: absolute; left: 16px; top: 40px; width: 260px; }
  .brand-name { font-family: "Arimo", Arial, sans-serif; font-weight: 700; font-size: 40px; color: #fff; letter-spacing: 1px; line-height: 1; }
  .brand-tag { font-family: "Arimo", Arial, sans-serif; font-weight: 700; font-size: 7.5px; color: #fff; letter-spacing: 5px; margin-top: 10px; padding-left: 36px; }
  .firm { position: absolute; left: 443px; top: 24px; }
  .firm-name { font-size: 20.5px; color: var(--blue); line-height: 1.1; letter-spacing: .2px; }
  .firm-title { font-family: "Arimo", Arial, sans-serif; font-size: 14.5px; color: var(--grey-text); margin-top: 2px; padding-left: 2px; }
  .firm-address { font-family: "Arimo", Arial, sans-serif; font-size: 13px; color: var(--grey-text); margin-top: 5px; line-height: 1.15; }
  .divider { position: absolute; left: 705px; top: 26px; width: 1.5px; height: 68px; background: var(--rule); }
  .contacts { position: absolute; left: 714px; top: 27px; list-style: none; font-family: "Arimo", Arial, sans-serif; font-size: 9.8px; color: var(--grey-text); }
  .contacts li { display: flex; align-items: center; height: 17.5px; }
  .contact-icon { width: 9px; height: 9px; margin-right: 3px; flex: none; }
  .date { position: absolute; left: 0; width: 843px; top: 157px; text-align: center; font-weight: 700; font-size: 16.5px; font-variant: small-caps; }
  .recipient { position: absolute; left: 58px; top: 210px; font-size: 12px; line-height: 15px; font-style: normal; }
  .via { font-weight: 700; font-style: italic; font-variant: small-caps; text-decoration: underline; }
  .reference { position: absolute; left: 112px; top: 317px; font-size: 12px; line-height: 15.3px; display: grid; grid-template-columns: 37px 108px auto; }
  .reference .heading { font-weight: 700; font-variant: small-caps; font-size: 13px; }
  .salutation { position: absolute; left: 58px; top: 394px; font-size: 12px; }
  .signoff { position: absolute; left: 634px; top: 938px; font-size: 14.6px; line-height: 19px; }
  .signature { position: absolute; left: 619px; top: 960px; width: 148px; height: 54px; background: linear-gradient(100deg, rgba(60,100,190,.08), rgba(60,100,190,.22), rgba(60,100,190,.08)); border-radius: 4px; }
  .signer { position: absolute; left: 634px; top: 1018px; font-size: 14.6px; line-height: 19px; }
  .signer em { font-style: italic; }
  .footer-bands { position: absolute; left: 0; top: 1100px; }
</style>
</head>
<body>
<div class="sheet">
  <header class="masthead">
    <svg class="masthead-shape" width="849" height="118" viewBox="0 0 849 118" aria-hidden="true">
      <polygon points="0,0 421,0 383,118 0,118" fill="var(--panel)"/>
      <polygon points="399,0 421,0 383,118 361,118" fill="var(--blue)"/>
    </svg>
    <div class="brand">
      <div class="brand-name">BRIX2KEY</div>
      <div class="brand-tag">OPEN THE RIGHT DOOR</div>
    </div>
    <div class="firm">
      <div class="firm-name">MARCUS T. DELGADO IV</div>
      <div class="firm-title">ATTORNEY AT LAW, PLLC</div>
      <div class="firm-address">2450 HARWOOD STREET SUITE 200<br>CEDAR RIDGE, TEXAS 75410</div>
    </div>
    <div class="divider"></div>
    <ul class="contacts">
      <li><svg class="contact-icon" viewBox="0 0 10 10" aria-hidden="true"><circle cx="5" cy="5" r="5" fill="var(--blue)"/><path d="M3.2 2.5l1 1-.5.7c.4.8 1 1.4 1.8 1.8l.7-.5 1 1-.6.9c-2 0-4.2-2.2-4.2-4.2z" fill="#fff"/></svg>(833) 555-0142</li>
      <li><svg class="contact-icon" viewBox="0 0 10 10" aria-hidden="true"><circle cx="5" cy="5" r="5" fill="var(--blue)"/><rect x="2.7" y="3.5" width="4.6" height="3.2" fill="#fff"/></svg>(512) 555-0187</li>
      <li><svg class="contact-icon" viewBox="0 0 10 10" aria-hidden="true"><circle cx="5" cy="5" r="5" fill="var(--blue)"/><path d="M2.6 3.4h4.8v3.2H2.6z M2.6 3.4L5 5.3l2.4-1.9" fill="#fff" stroke="var(--blue)" stroke-width=".5"/></svg>MARCUS@BRIX2KEY.NET</li>
      <li><svg class="contact-icon" viewBox="0 0 10 10" aria-hidden="true"><circle cx="5" cy="5" r="5" fill="var(--blue)"/><circle cx="5" cy="5" r="2.6" fill="none" stroke="#fff" stroke-width=".7"/><path d="M2.4 5h5.2M5 2.4v5.2" stroke="#fff" stroke-width=".5"/></svg>WWW.BRIX2KEY.COM</li>
    </ul>
  </header>

  <div class="date">July 11, 2021</div>

  <address class="recipient">
    <div class="via">Via Facsimile: (866)-555-0119</div>
    <div>Keystone Mutual Insurance</div>
    <div>Attn: Alan Pierce</div>
    <div>4820 Belt Line Road 310</div>
    <div>Pine Hollow, Texas 75562</div>
    <div>Tel: (737)-555-0163</div>
  </address>

  <div class="reference">
    <span class="heading">Re:</span><span class="heading" style="grid-column:2/4">Notice of Representation</span>
    <span></span><span>Claim Number:</span><span>2048316-TX</span>
    <span></span><span>Date of Accident:</span><span>March 14, 2019</span>
    <span></span><span>My client:</span><span>&nbsp;Sam Rivera</span>
  </div>

  <p class="salutation">Dear Mr. Alan Pierce,</p>

  <p class="signoff">Sincerely,</p>
  <div class="signature" role="img" aria-label="Handwritten signature of the attorney in blue ink"></div>
  <p class="signer">Marcus T. Delgado<br><em>Attorney at Law</em></p>

  <svg class="footer-bands" width="849" height="60" viewBox="0 0 849 60" aria-hidden="true">
    <polygon points="340,12 849,12 849,27 337,27" fill="var(--blue)"/>
    <polygon points="335,34 849,34 849,49 331,49" fill="var(--green)"/>
  </svg>
</div>
</body>
</html>
```